modern, IT themed business card for IT accelerator

Design a business card for tech oriented business accelerator. Prevailing color shall be orange.
we are operating in emerging markets and our mission is to provide co-working space, mentorship/coaching and ultimately seed financing IT startups.
also, we are helping financed ITs in obtaining next round financing, and to this end we are meeting with non IT/finance people and investment professionals..
that means card shall be designed to "impress" not only IT people (mostly liberal) but finance (more conservative)

Industry/Entity Type

Investment

Contact Information for Business Card

Company Name: Orin Venture Yard
Name: Levan Kutateli
Position: Partner
Address: 14, Marjanishvili Ave., Tbilisi 0112, Georgia
Tel: +995599348817
Email: l.kutateli@orinyard.ge
Website: www.orinyard.ge

Font styles to use
Sans Serif

Requirements
Must have
• Attached are logos of the company (portrait & landscape) choose any
Nice to have
• industry is IT and finance (in fact, financing IT startups). therefore design might have IT theme (inspiration from web or software designs)

```html
<!DOCTYPE html>
<html lang="en">
<head>
<meta charset="utf-8">
<title>Orin Venture Yard – Business Card</title>
<link href="https://fonts.googleapis.com/css2?family=Barlow:wght@500;600&display=swap" rel="stylesheet">
<style>
  :root {
    --page-bg: #f2f2f2;
    --card-light: #f4f4f5;
    --card-grey: #d9dadc;
    --orange: #f08a1c;
    --orange-deep: #b8621a;
    --orange-light: #f9b15e;
    --logo-grey: #6d6e71;
    --text-white: #ffffff;
    --text-glow: rgba(140, 66, 8, 0.85);
  }
  * { box-sizing: border-box; margin: 0; padding: 0; }
  html, body {
    width: 1200px; height: 900px; overflow: hidden;
    background: var(--page-bg);
    font-family: "Barlow", Arial, sans-serif;
  }
  .business-card {
    position: absolute; left: 100px; top: 160px;
    width: 1000px; height: 580px;
    border-radius: 40px; overflow: hidden;
    background: linear-gradient(120deg, var(--card-light) 40%, var(--card-grey) 100%);
    box-shadow: 0 18px 40px rgba(0,0,0,0.18);
  }
  .card-art { position: absolute; inset: 0; width: 100%; height: 100%; }
  .brand {
    position: absolute; left: 520px; top: 70px;
    display: flex; align-items: center; gap: 26px;
  }
  .brand-dot {
    width: 110px; height: 110px; border-radius: 50%;
    background: var(--orange);
  }
  .brand-name {
    color: var(--logo-grey); font-weight: 600;
    font-size: 50px; line-height: 1.05; letter-spacing: 1px;
    text-transform: uppercase;
  }
  .person {
    position: absolute; left: 60px; top: 235px;
    color: var(--text-white);
    text-shadow: 0 0 4px var(--text-glow), 0 0 2px var(--text-glow);
  }
  .person-name { font-size: 46px; font-weight: 600; }
  .person-role { font-size: 26px; font-weight: 500; margin-top: 4px; }
  .contact-list {
    position: absolute; left: 60px; top: 360px;
    list-style: none; color: var(--text-white);
    font-size: 30px; font-weight: 500;
    text-shadow: 0 0 4px var(--text-glow), 0 0 2px var(--text-glow);
  }
  .contact-item { display: flex; align-items: flex-start; gap: 12px; height: 44px; }
  .contact-item.address { height: auto; }
  .contact-icon { width: 32px; height: 32px; margin-top: 4px; flex: none; }
  .contact-icon * { fill: none; stroke: var(--text-white); stroke-width: 2.4; stroke-linejoin: round; stroke-linecap: round; }
</style>
</head>
<body>
  <div class="business-card">
    <svg class="card-art" viewBox="0 0 1000 580" role="img" aria-label="Abstract orange tech backdrop of layered translucent squares sweeping across the card">
      <defs>
        <linearGradient id="orange-sweep" x1="0" y1="0" x2="1" y2="1">
          <stop offset="0" stop-color="var(--orange-light)"/>
          <stop offset="0.45" stop-color="var(--orange)"/>
          <stop offset="1" stop-color="var(--orange-deep)"/>
        </linearGradient>
        <linearGradient id="orange-lower" x1="0" y1="0" x2="1" y2="1">
          <stop offset="0" stop-color="var(--orange)"/>
          <stop offset="1" stop-color="var(--orange-deep)"/>
        </linearGradient>
        <radialGradient id="bright-core" cx="0.42" cy="0.35" r="0.35">
          <stop offset="0" stop-color="#ffffff" stop-opacity="0.9"/>
          <stop offset="1" stop-color="#ffffff" stop-opacity="0"/>
        </radialGradient>
      </defs>
      <g fill="none" stroke="#c9cacc" stroke-opacity="0.5" stroke-width="3">
        <circle cx="640" cy="230" r="150"/>
        <circle cx="640" cy="230" r="220"/>
        <circle cx="640" cy="230" r="300"/>
      </g>
      <polygon points="0,0 330,0 560,580 0,580" fill="url(#orange-sweep)"/>
      <polygon points="520,420 1000,300 1000,580 580,580" fill="url(#orange-lower)" opacity="0.9"/>
      <rect width="1000" height="580" fill="url(#bright-core)"/>
    </svg>

    <div class="brand">
      <div class="brand-dot"></div>
      <div class="brand-name">Orin Venture<br>Yard</div>
    </div>

    <div class="person">
      <div class="person-name">Levan Kutateli</div>
      <div class="person-role">Partner</div>
    </div>

    <ul class="contact-list">
      <li class="contact-item">
        <svg class="contact-icon" viewBox="0 0 32 32"><path d="M8 4l5 6-3 3c2 4 5 7 9 9l3-3 6 5-3 4C14 27 5 18 4 7z"/></svg>
        <span>+995599348817</span>
      </li>
      <li class="contact-item">
        <svg class="contact-icon" viewBox="0 0 32 32"><rect x="3" y="8" width="26" height="17"/><path d="M3 8l13 10 13-10"/></svg>
        <span>l.kutateli@orinyard.ge</span>
      </li>
      <li class="contact-item">
        <svg class="contact-icon" viewBox="0 0 32 32"><circle cx="16" cy="16" r="12"/><ellipse cx="16" cy="16" rx="5" ry="12"/><path d="M4 16h24M6 10h20M6 22h20"/></svg>
        <span>www.orinyard.ge</span>
      </li>
      <li class="contact-item address">
        <svg class="contact-icon" viewBox="0 0 32 32"><path d="M3 16L16 5l13 11M7 13v14h18V13"/><path d="M13 27v-8h6v8"/></svg>
        <span>14, Marjanishvili Ave.,<br>Tbilisi 0112, Georgia</span>
      </li>
    </ul>
  </div>
</body>
</html>
```